Business Card Design Project

Need professional business card and Employee Badge design for a young dynamic and emp friendly IT Services company.

Target Market(s)

IT, Corporate

Industry/Entity Type

Business

Requirements
Must have
• Modern, Sleek, Prfessional, IT services
Should not have
• Too much diffrent colors

```html
<!DOCTYPE html>
<html lang="en">
<head>
<meta charset="utf-8">
<title>Kovira Technologies – Business Card</title>
<link href="https://fonts.googleapis.com/css2?family=Open+Sans:wght@400;600;700&display=swap" rel="stylesheet">
<style>
  :root {
    --brand-red: #c0182f;
    --ink-grey: #6e6e70;
    --text-dark: #4a4a4c;
    --card-white: #fbfbfb;
    --backdrop: #e6e4e1;
    --card-edge: #dcdcdc;
  }
  * { margin: 0; padding: 0; box-sizing: border-box; }
  html, body {
    width: 1200px; height: 900px; overflow: hidden;
    background: var(--backdrop);
    font-family: "Open Sans", Arial, sans-serif;
  }
  .canvas { position: relative; width: 1200px; height: 900px; }
  .card {
    position: absolute;
    width: 560px; height: 320px;
    background: var(--card-white);
    border: 1px solid var(--card-edge);
    box-shadow: 0 6px 18px rgba(0,0,0,0.12);
  }
  .card--front { left: 70px; top: 80px; }
  .card--back { left: 570px; top: 500px; }

  .wordmark {
    display: flex; align-items: center; gap: 12px;
    color: var(--brand-red);
    font-weight: 700;
    letter-spacing: 0.5px;
    white-space: nowrap;
  }
  .wordmark__square { width: 18px; height: 18px; background: var(--brand-red); flex: none; }
  .card--front .wordmark {
    position: absolute; left: 0; right: 0; top: 0; bottom: 0;
    justify-content: center; font-size: 38px;
  }
  .card--back .wordmark {
    position: absolute; left: 40px; top: 100px; font-size: 27px;
  }
  .wordmark__square--small { width: 14px; height: 14px; }

  .employee { position: absolute; left: 56px; top: 200px; }
  .employee__name {
    color: var(--brand-red); font-size: 15px; font-weight: 400; letter-spacing: 0.3px;
  }
  .employee__title { color: var(--ink-grey); font-size: 15px; }

  .contact {
    position: absolute; left: 350px; top: 96px;
    font-size: 12.5px; line-height: 1.45; color: var(--text-dark);
  }
  .contact__label { color: var(--brand-red); font-weight: 700; margin-right: 4px; }
  .contact__rule {
    width: 180px; height: 2px; background: var(--brand-red); margin: 8px 0 6px;
  }
  .contact__web { color: var(--ink-grey); }
  .contact__web strong { color: var(--brand-red); font-weight: 600; }
</style>
</head>
<body>
<main class="canvas">
  <section class="card card--front" aria-label="Card front">
    <div class="wordmark"><span class="wordmark__square"></span>Kovira Technologies</div>
  </section>

  <section class="card card--back" aria-label="Card back">
    <div class="wordmark"><span class="wordmark__square wordmark__square--small"></span>Kovira Technologies</div>
    <div class="employee">
      <p class="employee__name">EMPLOYEE NAME</p>
      <p class="employee__title">Title</p>
    </div>
    <div class="contact">
      <p><span class="contact__label">T</span>123.555.0147</p>
      <p><span class="contact__label">E</span>info@koviratech.com</p>
      <p>48 Alder Park Road,</p>
      <p>Brookvale, CA 90210</p>
      <div class="contact__rule"></div>
      <p class="contact__web">www.<strong>koviratech</strong>.com</p>
    </div>
  </section>
</main>
</body>
</html>
```